Design eines Praxisschilds für Hausarztpraxis
Zielgruppe
Hausarztpraxis, Zielgruppe sind die Bewohner vor Ort, bodenständig
Aufgabenstellung
Praxisschild entwerfen, es soll schlicht sein. Das angefügte Logo bitte verwenden, ggf. auch nur das Symbol ohne Namen verwenden und den Namen extra in schwarz aufführen.
Farben:
- schwarz
- Pantone 13-0645 Limeade
- Pantone 7726
Text:
Dr. med. Jonas Walbrecht
Facharzt für Innere Medizin
Facharzt für Allgemeinmedizin
Sprechzeiten:
Montag bis Freitag 07:30 – 12:00 Uhr
Dienstag und Donnerstag 17:00 – 19:00 Uhr
und nach Vereinbarung
Tel: 0761 83172
www.hausarzt-beispielau.de
Format quer (die Maße sind leider vorgegeben): 55,7 cm x 42,8 cm

```html
<!DOCTYPE html>
<html lang="de">
<head>
<meta charset="utf-8">
<title>Praxisschild – Dr. Jonas Walbrecht</title>
<link href="https://fonts.googleapis.com/css2?family=Fira+Sans:ital,wght@0,400;0,600;1,400&display=swap" rel="stylesheet">
<style>
  :root {
    --backdrop: #e9e9e6;
    --sign: #ffffff;
    --lime: #d3da5a;
    --green: #3d8a4e;
    --text-grey: #8c8c8a;
    --edge: #d6d6d2;
  }
  * { margin: 0; padding: 0; box-sizing: border-box; }
  html, body {
    width: 1200px;
    height: 800px;
    overflow: hidden;
    background: var(--backdrop);
    font-family: "Fira Sans", sans-serif;
  }
  .canvas {
    width: 1200px;
    height: 800px;
    display: flex;
    align-items: center;
    justify-content: center;
  }
  .practice-sign {
    position: relative;
    width: 990px;
    height: 761px;
    background: var(--sign);
    border: 1px solid var(--edge);
    overflow: hidden;
  }
  .brand-mark {
    position: absolute;
    left: 610px;
    top: 100px;
    width: 110px;
    height: 110px;
    border-radius: 50%;
    background: var(--green);
  }
  .practice-name {
    position: absolute;
    left: 340px;
    top: 262px;
    font-size: 64px;
    line-height: 1.1;
    font-weight: 600;
    color: var(--lime);
    letter-spacing: -0.5px;
    white-space: nowrap;
  }
  .info {
    position: absolute;
    left: 344px;
    top: 400px;
    color: var(--text-grey);
    font-size: 19px;
    line-height: 1.35;
    letter-spacing: 0.5px;
    white-space: nowrap;
  }
  .info .doctor,
  .info .label,
  .info .contact { font-style: italic; }
  .info .doctor,
  .info .label { font-size: 22px; }
  .info .block + .block { margin-top: 26px; }
  .info .contact { font-size: 21px; line-height: 1.3; }
</style>
</head>
<body>
<div class="canvas">
  <section class="practice-sign">
    <div class="brand-mark" aria-hidden="true"></div>
    <h1 class="practice-name">Dr. Jonas Walbrecht</h1>
    <div class="info">
      <div class="block">
        <p class="doctor">Dr. med. Jonas Walbrecht</p>
        <p>Facharzt für Innere Medizin</p>
        <p>Facharzt für Allgemeinmedizin</p>
      </div>
      <div class="block">
        <p class="label">Sprechzeiten:</p>
        <p>Montag bis Freitag 07:30 – 12:00 Uhr</p>
        <p>Dienstag und Donnerstag 17:00 – 19:00 Uhr</p>
        <p>und nach Vereinbarung</p>
      </div>
      <div class="block contact">
        <p>Tel: 0761 83172</p>
        <p>www.hausarzt-beispielau.de</p>
      </div>
    </div>
  </section>
</div>
</body>
</html>
```